Bramwell Business Cards

Logo files are included. Full "Bramwell" logo should be included on the back of the business card. The B symbol should be included on the front with the contact information.

Bramwell, LLC is the company name and we do commercial construction and real estate development consulting services. Look for a fairly simple card design utilizing our logo.

```html
<!DOCTYPE html>
<html lang="en">
<head>
<meta charset="utf-8">
<title>Bramwell Business Cards</title>
<link href="https://fonts.googleapis.com/css2?family=Arimo:wght@400;700&display=swap" rel="stylesheet">
<style>
  :root{
    --navy:#17364b;
    --gold:#ecae1d;
    --white:#ffffff;
    --ink:#1f1f1f;
    --stage:#2a2a2c;
  }
  *{box-sizing:border-box;margin:0;padding:0}
  html,body{width:1200px;height:1200px;overflow:hidden}
  body{background:var(--stage);font-family:"Arimo",Arial,sans-serif;position:relative}
  .card{position:absolute;top:215px;width:420px;height:770px;border-radius:30px;overflow:hidden}
  .card-front{left:150px;background:var(--white)}
  .card-back{left:630px;background:var(--navy)}

  .front-brand{position:absolute;top:0;left:0;right:0;height:330px;display:flex;align-items:center;justify-content:center;gap:16px}
  .brand-circle{width:46px;height:46px;border-radius:50%;border:6px solid var(--gold)}
  .front-brand .brand-name{font-size:52px;font-weight:700;color:var(--navy);letter-spacing:1px}

  .name-band{position:absolute;top:345px;left:0;right:0;height:98px;background:var(--navy);text-align:center;padding-top:22px}
  .person-name{color:var(--gold);font-weight:700;font-size:30px;letter-spacing:.5px}
  .person-title{color:var(--white);font-size:19px;margin-top:4px}

  .contact{position:absolute;top:478px;left:0;right:0;text-align:center;color:var(--ink)}
  .icon-row{display:flex;align-items:center;justify-content:center;gap:10px}
  .rule{height:1.5px;background:var(--gold);width:92px}
  .icon{width:32px;height:32px;border-radius:6px;background:var(--navy);display:flex;align-items:center;justify-content:center}
  .contact-lines{margin-top:16px;font-size:19px;line-height:27px}
  .divider{height:1.5px;background:var(--gold);width:270px;margin:14px auto}
  .address{font-size:19px;line-height:27px}

  .back-brand{position:absolute;left:50%;top:50%;transform:translate(-50%,-50%) rotate(-90deg);display:flex;align-items:center;gap:24px;white-space:nowrap}
  .back-brand .brand-circle{width:100px;height:100px;border-width:10px}
  .back-brand .brand-name{font-size:86px;font-weight:400;color:var(--white);letter-spacing:3px}
</style>
</head>
<body>
  <section class="card card-front">
    <div class="front-brand">
      <span class="brand-circle"></span>
      <span class="brand-name">Bramwell</span>
    </div>
    <div class="name-band">
      <p class="person-name">NORA WHITFIELD</p>
      <p class="person-title">Founder &amp; CEO</p>
    </div>
    <div class="contact">
      <div class="icon-row">
        <span class="rule"></span>
        <span class="icon"><svg width="18" height="18" viewBox="0 0 24 24"><path fill="#fff" d="M6.6 10.8a15 15 0 0 0 6.6 6.6l2.2-2.2c.3-.3.7-.4 1-.2 1.1.4 2.3.6 3.6.6.6 0 1 .4 1 1V20c0 .6-.4 1-1 1A17 17 0 0 1 3 4c0-.6.4-1 1-1h3.5c.6 0 1 .4 1 1 0 1.3.2 2.5.6 3.6.1.3 0 .7-.2 1z"/></svg></span>
        <span class="icon"><svg width="18" height="18" viewBox="0 0 24 24"><rect x="3" y="6" width="18" height="12" rx="1" fill="none" stroke="#fff" stroke-width="2"/><path d="M3 6l9 7 9-7M3 18l7-6M21 18l-7-6" fill="none" stroke="#fff" stroke-width="1.6"/></svg></span>
        <span class="icon"><svg width="18" height="18" viewBox="0 0 24 24"><circle cx="12" cy="12" r="9" fill="none" stroke="#fff" stroke-width="2"/><ellipse cx="12" cy="12" rx="4" ry="9" fill="none" stroke="#fff" stroke-width="1.5"/><path d="M3 12h18" stroke="#fff" stroke-width="1.5"/></svg></span>
        <span class="rule"></span>
      </div>
      <div class="contact-lines">
        <p>123-555-01840</p>
        <p>hello@bramwellco.com</p>
        <p>www.bramwellco.com</p>
      </div>
      <div class="divider"></div>
      <div class="address">
        <p>418 Granite Row</p>
        <p>Ashford County 7710</p>
      </div>
    </div>
  </section>

  <section class="card card-back">
    <div class="back-brand">
      <span class="brand-circle"></span>
      <span class="brand-name">BRAMWELL</span>
    </div>
  </section>
</body>
</html>
```